Flyer-Design für meine Tätigkeit als freier Trauerredner
Zielgruppe
Für meine Tatigkeit als freier Trauerredner bei Beerdigungen möchte ich einen Flyer designen lassen, um diesen bei Bestattern aufzulegen sowie diese grundsätzlich als Informationsmaterial an interessierte Personen weitergeben zu können. Zielgruppe sind einerseits Personen, die sich lange im Vorfeld Gedanken über den Tod machen und den Wunsch äußern, im Rahmen einer persönlichen Gedenkfeier, unabhängig einer Konfessionszugehörigkeit und der Kirche verabschiedet zu werden. Auf der anderen Seite ist der Flyer ebenso für trauendernde Angehörige gedacht, die aufgrund eines unerwarteten Todesfalls sich mit dem Thema Beerdigung auseinadersetzen müssen und nach Alternativen zu einer krichlichen Beerdiugung suchen.
Aufgabenstellung
Eine Visitenkarte scheint mir im Format zu klein ... ein Flyer in einem größeren Format scheint mir geeigneter, Informationen zu vermitteln. Eine große Stärke von mir ist meine Emapthie. Der Flyer soll dies in der Bildsprache ausdrücken. Ebenso soll der Flyer durch die Bilder und die gewählte Sprahce Vertrauen aufbauen. Tod und Beerdigung sind für viele ein Tabuthemen ... der Flyer soll hier eine Brücke schlagen.
Wichtig wäre mir den Ablauf der Vorbereitung im Flyer aufzuskizzieren, um zu wissen, wie die Vorbereitung und Druchführung beispielhaft erfolgt.
Meine Kernaussage:
Freie Trauerreden, so einzigartig und besonders wie jeder Mensch selbst!
Als freier Trauerredner ist es mein Anspruch, den schweren Moment des Abschiednehmens so persönlich und würdevoll wie nur möglich zu gestalten!
Mein Ziel: Herzensverbindungen zwischen Menschen aufleben zu lassen und diese zu stärken. Herzensverbindungen leben und wirken weiter – unabhängig ob im Leben oder über den Tod hinaus!
Alle Informationen, die im Flyer aufgeführt werden sollen, sind dem beigefügten Word-Dokument zu entnehmen.
Wichtige Information finden Sie auf meiner Website www.tobiaskrämer.com
Wenn ein Statement oder Reszession benötigt wird und sich gut im Flyer macht, liefere ich diese gerne nach.

```html
<!DOCTYPE html>
<html lang="de">
<head>
<meta charset="utf-8">
<title>Tobias Krämer – Freier Trauerredner – Flyer</title>
<link rel="stylesheet" href="https://fonts.googleapis.com/css2?family=Source+Sans+3:ital,wght@0,300;0,400;0,600;1,400;1,600&display=swap">
<style>
  :root {
    --stage: #4b4b4b;
    --paper: #6f6f6f;
    --ribbon: #9b1a1f;
    --accent-text: #d8322d;
    --light-text: #ffffff;
    --muted-text: #cfcfcf;
    --kontakt: #515151;
    --quote-box: #8a8a8a;
    --photo-a: #4e4d5a;
    --photo-b: #7d6f6c;
  }
  * { box-sizing: border-box; margin: 0; padding: 0; }
  html, body { width: 1200px; height: 849px; overflow: hidden; }
  body {
    background: var(--stage);
    font-family: "Source Sans 3", "Helvetica Neue", Arial, sans-serif;
    color: var(--light-text);
    position: relative;
  }
  .sheet-frame {
    position: absolute;
    top: 218px;
    width: 580px;
    height: 414px;
    overflow: hidden;
    box-shadow: 0 6px 18px rgba(0,0,0,.35);
  }
  .sheet-frame--outside { left: 13px; }
  .sheet-frame--inside { left: 607px; }
  .sheet {
    position: absolute;
    top: 0; left: 0;
    background: var(--paper);
    transform-origin: 0 0;
  }
  .sheet--outside { width: 767px; height: 546px; transform: scale(0.7562); }
  .sheet--inside { width: 775px; height: 551px; transform: scale(0.7484); }
  .sheet svg.artwork { position: absolute; top: 0; left: 0; }

  /* outside */
  .brand { position: absolute; left: 484px; top: 32px; }
  .brand__name { font-size: 20px; font-weight: 400; letter-spacing: 9.5px; }
  .brand__role { font-size: 19px; font-weight: 400; letter-spacing: 3.6px; margin-top: -2px; }
  .motto { position: absolute; left: 26px; top: 222px; list-style: none; }
  .motto li { font-size: 20px; font-weight: 300; color: var(--muted-text); line-height: 42.5px; }
  .claim { position: absolute; right: 20px; top: 326px; text-align: right; }
  .claim__headline { font-size: 12.5px; line-height: 15px; }
  .claim__text { font-size: 7.6px; font-style: italic; line-height: 11px; margin-top: 7px; }
  .contact { position: absolute; left: 38px; top: 450px; display: flex; gap: 16px; }
  .contact__label { font-size: 13px; font-style: italic; color: var(--kontakt); letter-spacing: .5px; }
  .contact__details { font-size: 8px; font-weight: 600; line-height: 12.5px; padding-top: 1px; }
  .quote {
    position: absolute; left: 410px; top: 444px; width: 338px; height: 70px;
    background: var(--quote-box); border-radius: 35px;
    display: flex; align-items: center; justify-content: center;
    padding: 0 22px; text-align: center;
    font-size: 7.8px; font-style: italic; line-height: 12.5px;
  }

  /* inside */
  .column { position: absolute; top: 124px; }
  .column--info { left: 31px; width: 328px; }
  .column--process { left: 409px; width: 350px; }
  .info-heading { color: var(--accent-text); font-size: 8.8px; font-weight: 400; margin-top: 11px; line-height: 12px; }
  .info-heading:first-child { margin-top: 0; }
  .info-text { font-size: 8.3px; line-height: 12.6px; letter-spacing: -.25px; }
  .info-list { font-size: 8.3px; line-height: 12.6px; letter-spacing: -.25px; padding-left: 33px; }
  .info-list li::marker { font-size: 6px; }
  .info-gap { margin-top: 12px; }
  .process-title { font-size: 12px; font-weight: 400; letter-spacing: .8px; margin-bottom: 8px; }
  .step-heading { color: var(--accent-text); font-size: 9px; font-weight: 400; letter-spacing: 1.1px; margin-top: 9px; line-height: 12px; }
  .step-heading:first-of-type { margin-top: 0; }
  .step-heading small { color: var(--light-text); font-size: 5.5px; font-weight: 600; margin-left: 10px; letter-spacing: .4px; }
  .step-text { font-size: 8.2px; line-height: 12.7px; font-weight: 600; letter-spacing: .85px; }
  .step-list { font-size: 8.2px; line-height: 12.7px; font-weight: 600; letter-spacing: .85px; padding-left: 32px; }
  .step-list li::marker { font-size: 6px; }
  .footnote { font-size: 5px; font-weight: 600; margin-top: 10px; padding-left: 16px; letter-spacing: .3px; }
</style>
</head>
<body>

<section class="sheet-frame sheet-frame--outside" aria-label="Flyer Außenseite">
  <div class="sheet sheet--outside">
    <svg class="artwork" width="767" height="546" viewBox="0 0 767 546">
      <defs>
        <linearGradient id="photo-tone" x1="0" y1="0" x2="1" y2="1">
          <stop offset="0" stop-color="var(--photo-a)"/>
          <stop offset="1" stop-color="var(--photo-b)"/>
        </linearGradient>
        <clipPath id="photo-window">
          <polygon points="290,0 767,0 767,235 595,140 385,360 170,140"/>
        </clipPath>
        <filter id="ribbon-shadow" x="-10%" y="-10%" width="120%" height="130%">
          <feDropShadow dx="0" dy="4" stdDeviation="4" flood-color="#000" flood-opacity=".45"/>
        </filter>
      </defs>
      <rect x="120" y="0" width="647" height="420" fill="url(#photo-tone)" clip-path="url(#photo-window)"
            role="img" aria-label="Platz für Foto: Mann in Rückansicht auf einem verschneiten Feld im Abendlicht"/>
      <polyline points="300,-20 160,135 385,378 595,163 790,268" fill="none"
                stroke="var(--ribbon)" stroke-width="48" stroke-linejoin="round" filter="url(#ribbon-shadow)"/>
    </svg>

    <header class="brand">
      <h1 class="brand__name">TOBIAS KRÄMER</h1>
      <p class="brand__role">Freier Trauerredner</p>
    </header>

    <ul class="motto">
      <li>LICHTVOLLE -</li>
      <li>WÜRDEVOLLE -</li>
      <li>PERSÖNLICHE WEGE</li>
      <li>DES ABSCHIEDS</li>
    </ul>

    <div class="claim">
      <p class="claim__headline">Freie Gedenkfeiern, so einzigartig und<br>besonders wie jeder Mensch selbst!</p>
      <p class="claim__text">Mein Ziel ist es, Herzensverbindungen zwischen<br>Menschen aufleben zu lassen und zu stärken.<br>Herzensverbindungen leben und wirken weiter –<br>unabhängig ob im Leben oder über den Tod hinaus!</p>
    </div>

    <div class="contact">
      <p class="contact__label">KONTAKT</p>
      <p class="contact__details">Tobias Krämer<br>Lindenweg 8 | 84130 Dingolfeld<br>Telefon/WhatsApp/Telegram: 0170 5550182<br>eMail: info@tobiaskrämer.com | Internet: www.tobiaskrämer.com</p>
    </div>

    <blockquote class="quote">„Freier Trauerredner zu sein ist meine Berufung! Mir ist es eine Freude, Menschen Halt und Kraft zu geben! Das ist mein Anspruch – sowohl als freier Trauerredner im Moment des Abschiednehmens, aber auch als Coach, wenn es darum geht, wieder Halt und Kraft im Leben zu finden!“</blockquote>
  </div>
</section>

<section class="sheet-frame sheet-frame--inside" aria-label="Flyer Innenseite">
  <div class="sheet sheet--inside">
    <svg class="artwork" width="775" height="551" viewBox="0 0 775 551">
      <defs>
        <filter id="ribbon-shadow-small" x="-10%" y="-10%" width="120%" height="130%">
          <feDropShadow dx="0" dy="3" stdDeviation="3" flood-color="#000" flood-opacity=".45"/>
        </filter>
      </defs>
      <polyline points="615,-10 574,38 640,116 716,55 790,118" fill="none"
                stroke="var(--ribbon)" stroke-width="22" stroke-linejoin="round" filter="url(#ribbon-shadow-small)"/>
    </svg>

    <div class="column column--info">
      <h2 class="info-heading">Was ist eine freie Trauerfeier/Gedenkfeier?</h2>
      <p class="info-text">Freie Trauerzeremonie, Gedenkfeier, Beerdigung, Lebensabschiedsfeier… Synonyme für eine, von mir als freier Trauerredner durchgeführte, Abschiedszeremonie, die ganz individuell und persönlich auf die verstorbene Person oder das verstorbene Kind bezogen ist – weltlich frei, unabhängig einer Konfession mit individuellem Ablauf.</p>

      <h2 class="info-heading">Orte für freie Trauerfeiern</h2>
      <p class="info-text">Freie Trauerfeiern finden meist auf Friedhöfen, in Kapellen oder Aussegnungshallen, auf dem Friedhofsgelände, einem Waldfriedhof oder auch in den eigenen Räumen des Bestatters statt. Auch ein selbstgewählter Ort in der Natur kann unter bestimmten Voraussetzungen möglich sein.</p>

      <p class="info-text info-gap">Eine freie Trauerzeremonie beinhaltet im Wesentlichen folgenden Elemente:</p>
      <ul class="info-list">
        <li>Gedenken an die verstorbene Person in einem feierlichen Rahmen</li>
        <li>Herausstellen der einzigartigen Persönlichkeit und den Charakter der Person – würdevoll wird dies in den Mittelpunkt der Feier gestellt</li>
        <li>Aufleben lassen wertvoller Erinnerungen und Ausdruck der Dankbarkeit an die gemeinsamen Stunden und damit Stärkung der Herzensverbindung</li>
        <li>der Trauer Raum zu geben und die freie Trauerfeier Bestandteil des Aufarbeitungsprozesses werden zu lassen</li>
        <li>Beistand, Trost und Zuspruch erfahren – durch die anwesenden Trauergäste, den freien Trauerredner, alles Verbindende und/oder das Göttliche</li>
      </ul>

      <h2 class="info-heading">Dauer einer freien Traufeier</h2>
      <p class="info-text">Eine freie Trauerfeier dauert in der Regel 20 - 30 Minuten.</p>

      <h2 class="info-heading">Kosten der Trauerrede / Gedenkfeier</h2>
      <p class="info-text">Die Kosten für die Trauerrede, bzw. der Umrahmung Gedenkfeier betragen 439 EUR inkl. MwSt. Die Pauschale beinhaltet das Vorbereitungsgespräch sowie die Aufbereitung und Durchführung der freien Trauerrede, die Sie zum Nachlesen als persönliches Exemplar erhalten. Die Fahrtkosten betragen 55 Cent je Kilometer für die Fahrt zum Friedhof bzw. Ort der Verabschiedung und zurück.</p>
    </div>

    <div class="column column--process">
      <h2 class="process-title">Vorbereitung und Ablauf</h2>

      <h3 class="step-heading">1. ÜBERLEGUNGEN IM VORFELD:</h3>
      <p class="step-text">Es ist gut, im ersten Schritt der Planung einer freien Trauerfeier grundsätzlichen Überlegungen Raum zu geben, wie zum Beispiel:</p>
      <ul class="step-list">
        <li>Hat die/der Verstorbene im Vorfeld Wünsche zur eigenen Beerdigung geäußert?</li>
        <li>Wie sollte die freie Trauerfeier ablaufen, damit die Gedenkfeier „stimmig“ ist – für die verstorbene Person, Sie selbst, Familie, Freunde und wie sie diese später in guter Erinnerung behalten?</li>
      </ul>

      <h3 class="step-heading">2. DAS VORBEREITUNGSGESPRÄCH<small>Dauer ca. 2 Stunden</small></h3>
      <p class="step-text">Persönlich, telefonisch oder digital werden in einem Vorbereitungsgespräch alle wichtigen Informationen zur verstorbenen Person gesammelt und gemeinsam der Ablauf der freien Gedenkfeier geplant.</p>

      <h3 class="step-heading">3. ABLAUF DER GEDENKFEIER<small>Dauer ca. 20 – 30 Minuten</small></h3>
      <p class="step-text">Den Möglichkeiten des Ablaufs einer freien Trauerfeier sind wenig Grenzen gesetzt – ihre Bedürfnisse und Wünsche stehen im Mittelpunkt!<br>Wichtige Elemente:</p>
      <ul class="step-list">
        <li>Persönliche Worte in Form einer individuellen Trauerrede zur Würdigung des Lebens der verstorbenen Person</li>
        <li>Ausgewählte Musikstücke</li>
        <li>Aktive Beteiligung Ihrerseits, von Angehörigen und/oder Freunden durch das Vorlesen eines Gedichts, eines Gebets oder persönlich verfasster Worte</li>
        <li>Rituale des Gedenkens können einen würdevollen, persönlichen Beitrag umrahmen und in verschiedenster Weise integriert werden, z.B. Seifenblasen, Briefe/Wünsche, eine Lichterkranz der Verbundenheit oder Wunderkerzen zum Schluss einer Gedenkfeier.</li>
      </ul>
      <p class="footnote">Detailinformationen zu den einzelnen Punkten finden Sie im Internet unter www.tobiaskrämer.com</p>
    </div>
  </div>
</section>

</body>
</html>
```